Website for Apartment Rental in Prague

I would like to create designs of my website focused on luxury apartment rentals in Prague, Czech Republic. I created initial mock-ups, They are all attached. I need to design homepage and subpage. The mock-ups were created by combining elements from different websites that I liked but I need you to create a design that is unique and original. The attached files a only a guidance for the structure of the website but not for the design. Try to be creative.

Industry/Entity Type

Apartment

```html
<!DOCTYPE html>
<html lang="en">
<head>
<meta charset="utf-8">
<title>Lumen. – Apartments &amp; Rates</title>
<link href="https://fonts.googleapis.com/css2?family=Cormorant+Garamond:wght@500;600&family=Jost:wght@400;500&display=swap" rel="stylesheet">
<style>
:root{
  --ink:#16202a;
  --ink-soft:#2a3642;
  --text:#3b4550;
  --muted:#8b929a;
  --brass:#b08d57;
  --brass-dark:#96743f;
  --cream:#f7f3ec;
  --sand:#ece4d6;
  --line:#e3dccf;
  --white:#ffffff;
}
*{margin:0;padding:0;box-sizing:border-box}
html,body{width:1200px;height:2473px;overflow:hidden;background:var(--white)}
body{position:relative;font-family:"Jost",sans-serif;color:var(--text);font-size:13px}
.abs{position:absolute}
.serif{font-family:"Cormorant Garamond",serif}
svg{display:block;flex:none}

/* header */
.topbar{left:89px;width:1022px;top:24px;height:34px;display:flex;align-items:center;font-size:12px;color:var(--text)}
.topbar .contact{display:flex;gap:22px;align-items:center}
.topbar .contact span{display:flex;align-items:center;gap:7px;white-space:nowrap}
.brand{position:absolute;left:50%;transform:translateX(-50%);font-family:"Cormorant Garamond",serif;font-weight:600;font-size:32px;line-height:34px;color:var(--ink);white-space:nowrap}
.topbar .links{margin-left:auto;display:flex;align-items:center;gap:12px;white-space:nowrap}
.topbar .sep{width:1px;height:14px;background:var(--line)}
.rule-top{left:89px;width:1022px;top:77px;height:1px;background:var(--line)}
.mainnav{left:0;width:1200px;top:78px;height:50px;display:flex;justify-content:center;gap:28px;font-weight:500;font-size:11.5px;letter-spacing:1.4px;text-transform:uppercase;align-items:center}
.mainnav a{color:var(--ink);text-decoration:none;position:relative;height:50px;display:flex;align-items:center;white-space:nowrap}
.mainnav a.active{color:var(--brass)}
.mainnav a.active::after{content:"";position:absolute;left:50%;bottom:9px;width:5px;height:5px;margin-left:-2.5px;border-radius:50%;background:var(--brass)}

.hero{left:0;top:128px;width:1200px;height:441px;background:linear-gradient(165deg,#2a1e1a 0%,#3b2a22 28%,#1c5fb8 52%,#2496e6 66%,#5a3a2a 88%,#2a1a14 100%)}

.steps{left:0;width:1200px;top:569px;height:57px;background:var(--cream);border-bottom:1px solid var(--line);display:flex;justify-content:center;gap:44px;align-items:center;font-weight:500;font-size:11.5px;letter-spacing:1.4px;text-transform:uppercase;color:var(--ink)}
.steps span{position:relative;height:57px;display:flex;align-items:center;white-space:nowrap}
.steps .active{color:var(--brass)}
.steps .active::after{content:"";position:absolute;left:0;right:0;bottom:-1px;height:2px;background:var(--brass)}

/* sidebar */
.sidebar{left:89px;top:676px;width:254px;height:900px}
.side-h{font-family:"Cormorant Garamond",serif;font-weight:600;font-size:24px;line-height:28px;color:var(--ink)}
.side-sub{font-size:13px;margin-top:4px}
.map{margin-top:18px;width:254px;height:240px;background:linear-gradient(135deg,#e8e4dc 0%,#efe6cf 50%,#cfe5b8 100%)}
.bedrooms{margin-top:36px}
.bedrooms ul{list-style:none;margin-top:12px;border-top:1px solid var(--line)}
.bedrooms li{font-size:13px;height:34px;display:flex;align-items:center;justify-content:space-between;border-bottom:1px solid var(--line);color:var(--ink)}
.selection{position:absolute;left:0;top:560px;width:254px;height:330px;background:var(--ink);color:var(--cream);padding:0 22px}
.sel-head{display:flex;justify-content:space-between;align-items:center;height:58px;font-weight:500;font-size:11px;letter-spacing:1.2px;text-transform:uppercase;border-bottom:1px solid var(--ink-soft)}
.sel-head .add{color:var(--brass)}
.room{display:flex;align-items:center;justify-content:space-between;height:50px}
.room .name{font-family:"Cormorant Garamond",serif;font-weight:600;font-size:20px}
.room .icons{display:flex;gap:8px}
.room .icons i{width:22px;height:22px;border-radius:50%;border:1px solid #4a5662;display:flex;align-items:center;justify-content:center}
.fields{display:grid;grid-template-columns:100px 100px;column-gap:10px}
.fields label{font-size:11.5px;height:22px;display:flex;align-items:center;color:#b9bfc6}
.select{height:34px;border:1px solid #3e4a56;font-size:12px;display:flex;align-items:center;justify-content:space-between;padding:0 8px;margin-bottom:12px;white-space:nowrap;color:var(--cream)}
.btn{background:var(--brass);color:var(--white);font-weight:500;font-size:11.5px;letter-spacing:1.2px;text-transform:uppercase;display:flex;align-items:center;justify-content:center;gap:16px;white-space:nowrap}
.selection .btn{height:42px;margin-top:6px}

/* apartment cards */
.apt{left:385px;width:726px;height:632px;background:var(--cream);padding:32px}
.apt-title{font-family:"Cormorant Garamond",serif;font-weight:600;font-size:32px;line-height:36px;color:var(--ink)}
.apt-price{font-weight:500;font-size:12px;letter-spacing:1.2px;color:var(--brass);margin-top:6px;text-transform:uppercase}
.more{position:absolute;right:32px;top:38px;height:40px;padding:0 18px;border:1px solid var(--ink);display:flex;align-items:center;gap:14px;font-weight:500;font-size:11px;letter-spacing:1.2px;text-transform:uppercase;color:var(--ink);white-space:nowrap}
.tabs{position:absolute;top:120px;left:32px;display:flex;gap:28px;font-weight:500;font-size:11.5px;letter-spacing:1.2px;text-transform:uppercase;color:var(--ink)}
.tabs span{padding-bottom:8px;position:relative;white-space:nowrap}
.tabs .active{color:var(--brass)}
.tabs .active::after{content:"";position:absolute;left:0;right:0;bottom:0;height:2px;background:var(--brass)}
.apt-text{position:absolute;top:168px;left:32px;width:662px;font-size:13.5px;line-height:24px}
.gallery{position:absolute;top:284px;left:32px;width:662px;height:220px}
.gallery .ph{position:absolute;top:0;height:220px}
.next{position:absolute;left:608px;top:88px;width:44px;height:44px;border-radius:50%;background:var(--white);display:flex;align-items:center;justify-content:center;box-shadow:0 2px 8px rgba(22,32,42,.18)}
.dates{position:absolute;top:524px;left:32px;width:662px;height:76px;background:var(--white)}
.dates .col{position:absolute;top:18px}
.dates .lbl{font-weight:500;font-size:10.5px;letter-spacing:1.2px;text-transform:uppercase;color:var(--ink)}
.dates .val{font-family:"Cormorant Garamond",serif;font-weight:600;font-size:18px;color:var(--muted);margin-top:2px}
.dates .div{position:absolute;left:168px;top:16px;width:1px;height:44px;background:var(--line)}
.dates .btn{position:absolute;right:16px;top:16px;width:236px;height:44px}

/* footer */
.footer{left:0;top:2080px;width:1200px;height:338px;background:var(--ink);color:#c3c8ce}
.foot-brand{position:absolute;left:89px;top:70px;font-family:"Cormorant Garamond",serif;font-weight:600;font-size:36px;line-height:40px;color:var(--cream)}
.foot-contact{position:absolute;left:89px;top:137px;list-style:none}
.foot-contact li{display:flex;align-items:center;gap:9px;height:32px;font-size:13px;white-space:nowrap}
.foot-col{position:absolute;top:84px}
.foot-col h4{font-family:"Cormorant Garamond",serif;font-weight:600;font-size:21px;color:var(--cream);margin-bottom:18px}
.foot-col ul{list-style:none}
.foot-col li{height:32px;display:flex;align-items:center;font-size:13px}
.foot-col p{font-size:13px;line-height:23px;width:300px}
.news{position:absolute;left:783px;top:206px;display:flex}
.news .input{width:216px;height:44px;background:var(--ink-soft);display:flex;align-items:center;gap:9px;padding-left:14px;font-size:12px;color:#a7aeb6}
.news .btn{width:112px;height:44px}
.copyright{left:0;width:1200px;top:2418px;height:55px;background:#101820;color:#8b929a;display:flex;align-items:center;justify-content:center;font-size:12px;letter-spacing:.4px}
</style>
</head>
<body>

<header>
  <div class="abs topbar">
    <div class="contact">
      <span><svg width="13" height="10" viewBox="0 0 12 10"><rect x="0.6" y="0.6" width="10.8" height="8.8" fill="none" stroke="#b08d57" stroke-width="1.2"/><path d="M1 1.2 6 5.4 11 1.2" fill="none" stroke="#b08d57" stroke-width="1.2"/></svg>stay@lumenrooms.com</span>
      <span><svg width="12" height="12" viewBox="0 0 12 12"><path d="M2.5 1 4.6 1 5.4 3.6 4 4.6C4.8 6.3 5.7 7.2 7.4 8L8.4 6.6 11 7.4 11 9.5C11 10.4 10.3 11 9.5 11 5 11 1 7 1 2.5 1 1.7 1.6 1 2.5 1Z" fill="none" stroke="#b08d57" stroke-width="1.1"/></svg>+420 555 018 240</span>
      <span>ENGLISH <svg width="8" height="5" viewBox="0 0 8 5"><path d="M1 1 4 4 7 1" fill="none" stroke="#16202a" stroke-width="1.4"/></svg></span>
    </div>
    <div class="brand">Lumen.</div>
    <div class="links">
      <span>Discover Prague</span><span class="sep"></span><span>Our Hospitality</span>
      <svg style="margin-left:8px" width="14" height="14" viewBox="0 0 13 13"><circle cx="5.5" cy="5.5" r="4.3" fill="none" stroke="#16202a" stroke-width="1.5"/><path d="M8.7 8.7 12 12" stroke="#16202a" stroke-width="1.6"/></svg>
    </div>
  </div>
  <div class="abs rule-top"></div>
  <nav class="abs mainnav">
    <a>Home</a><a class="active">Apartments</a><a>Location</a><a>Services</a><a>Gallery</a><a>News</a><a>Exclusive Offers &amp; Tours</a><a>For Families</a><a>Contact Us</a>
  </nav>
</header>

<div class="abs hero" role="img" aria-label="Rooftop swimming pool lit blue at dusk with white sun loungers"></div>

<nav class="abs steps">
  <span class="active">Apartments &amp; Rates</span><span>Stay Enhancement</span><span>Guest Details</span><span>Review</span><span>Checkout</span>
</nav>

<aside class="abs sidebar">
  <div class="side-h">Address</div>
  <div class="side-sub">Some address line goes here..</div>
  <div class="map" role="img" aria-label="Street map showing the apartment location"></div>
  <div class="bedrooms">
    <div class="side-h">Search by Bedrooms</div>
    <ul>
      <li>1 Bedroom Apartment<svg width="6" height="9" viewBox="0 0 5 8"><path d="M1 1 4 4 1 7" fill="none" stroke="#b08d57" stroke-width="1.3"/></svg></li>
      <li>2 Bedroom Apartment<svg width="6" height="9" viewBox="0 0 5 8"><path d="M1 1 4 4 1 7" fill="none" stroke="#b08d57" stroke-width="1.3"/></svg></li>
      <li>3 Bedroom Apartment<svg width="6" height="9" viewBox="0 0 5 8"><path d="M1 1 4 4 1 7" fill="none" stroke="#b08d57" stroke-width="1.3"/></svg></li>
      <li>4 Bedroom Apartment<svg width="6" height="9" viewBox="0 0 5 8"><path d="M1 1 4 4 1 7" fill="none" stroke="#b08d57" stroke-width="1.3"/></svg></li>
      <li>Studio<svg width="6" height="9" viewBox="0 0 5 8"><path d="M1 1 4 4 1 7" fill="none" stroke="#b08d57" stroke-width="1.3"/></svg></li>
    </ul>
  </div>
  <div class="selection">
    <div class="sel-head"><span>Your Selection</span><span class="add">+Add Apartment</span></div>
    <div class="room"><span class="name">Room 1</span>
      <span class="icons">
        <i><svg width="8" height="8" viewBox="0 0 8 8"><path d="M1 1 7 7M7 1 1 7" stroke="#f7f3ec" stroke-width="1.2"/></svg></i>
        <i><svg width="8" height="2" viewBox="0 0 8 2"><path d="M0 1H8" stroke="#f7f3ec" stroke-width="1.2"/></svg></i>
      </span>
    </div>
    <div class="fields">
      <label>Arrival:</label><label>Departure:</label>
      <div class="select">30th Dec 2017<svg width="8" height="5" viewBox="0 0 8 5"><path d="M1 1 4 4 7 1" fill="none" stroke="#b08d57" stroke-width="1.4"/></svg></div>
      <div class="select">03rd Jan 2018<svg width="8" height="5" viewBox="0 0 8 5"><path d="M1 1 4 4 7 1" fill="none" stroke="#b08d57" stroke-width="1.4"/></svg></div>
      <label>Adults:</label><label>Kids/Infants:</label>
      <div class="select">05<svg width="8" height="5" viewBox="0 0 8 5"><path d="M1 1 4 4 7 1" fill="none" stroke="#b08d57" stroke-width="1.4"/></svg></div>
      <div class="select">08<svg width="8" height="5" viewBox="0 0 8 5"><path d="M1 1 4 4 7 1" fill="none" stroke="#b08d57" stroke-width="1.4"/></svg></div>
    </div>
    <div class="btn">Check Availability <svg width="14" height="8" viewBox="0 0 12 8"><path d="M0 4H11M8 1 11 4 8 7" fill="none" stroke="#fff" stroke-width="1.2"/></svg></div>
  </div>
</aside>

<section class="abs apt" style="top:676px">
  <h2 class="apt-title">1 Bedroom Apartment</h2>
  <div class="apt-price">From $150/Night</div>
  <div class="more">More Information <svg width="14" height="8" viewBox="0 0 12 8"><path d="M0 4H11M8 1 11 4 8 7" fill="none" stroke="#16202a" stroke-width="1.2"/></svg></div>
  <div class="tabs"><span class="active">Apartment Description</span><span>Apartment Amenities</span></div>
  <p class="apt-text">Aenean commodo ligula eget dolor aenean massa cum sociis natoque penatibus et magnis dis parturient montes nascetur ridiculus mus donec quam felis ultricies nec pellentesque eu pretium quis sem nulla consequat massa quis enim donec pede justo fringilla vel aliquet nec dictum.</p>
  <div class="gallery">
    <div class="ph" style="left:0;width:260px;background:linear-gradient(135deg,#d9d6d2,#8f8b86 60%,#4a4644)" role="img" aria-label="Open-plan bedroom with grey floor and turquoise bedding"></div>
    <div class="ph" style="left:268px;width:260px;background:linear-gradient(135deg,#f3f1ee,#d6bfa0 55%,#8a6a48)" role="img" aria-label="White living corner with wooden shelving and colourful prints"></div>
    <div class="ph" style="left:536px;width:126px;background:linear-gradient(135deg,#f4f4f4,#d2d2d2)" role="img" aria-label="Bright white room interior"></div>
    <div class="next"><svg width="14" height="8" viewBox="0 0 12 8"><path d="M0 4H11M8 1 11 4 8 7" fill="none" stroke="#16202a" stroke-width="1.2"/></svg></div>
  </div>
  <div class="dates">
    <div class="col" style="left:24px"><div class="lbl">Checkin Date:</div><div class="val">11th Nov 2017</div></div>
    <div class="div"></div>
    <div class="col" style="left:190px"><div class="lbl">Checkout Date:</div><div class="val">18th Nov 2017</div></div>
    <div class="btn">Check Rates &amp; Availability <svg width="14" height="8" viewBox="0 0 12 8"><path d="M0 4H11M8 1 11 4 8 7" fill="none" stroke="#fff" stroke-width="1.2"/></svg></div>
  </div>
</section>

<section class="abs apt" style="top:1340px">
  <h2 class="apt-title">1 Bedroom Apartment</h2>
  <div class="apt-price">From $80.50/Night</div>
  <div class="more">More Information <svg width="14" height="8" viewBox="0 0 12 8"><path d="M0 4H11M8 1 11 4 8 7" fill="none" stroke="#16202a" stroke-width="1.2"/></svg></div>
  <div class="tabs"><span class="active">Apartment Description</span><span>Apartment Amenities</span></div>
  <p class="apt-text">Aenean commodo ligula eget dolor aenean massa cum sociis natoque penatibus et magnis dis parturient montes nascetur ridiculus mus donec quam felis ultricies nec pellentesque eu pretium quis sem nulla consequat massa quis enim donec pede justo fringilla vel aliquet nec dictum.</p>
  <div class="gallery">
    <div class="ph" style="left:0;width:260px;background:linear-gradient(135deg,#e6e2dc,#b9b6b2 50%,#2e2e2e)" role="img" aria-label="Grey sofa with patterned and yellow cushions beside a dark coffee table"></div>
    <div class="ph" style="left:268px;width:260px;background:linear-gradient(135deg,#f1efec,#c9c6c0 50%,#b07a45)" role="img" aria-label="Bright living room with wooden floor and large windows"></div>
    <div class="ph" style="left:536px;width:126px;background:linear-gradient(135deg,#f5f5f5,#d6d6d6)" role="img" aria-label="White room with tall windows"></div>
    <div class="next"><svg width="14" height="8" viewBox="0 0 12 8"><path d="M0 4H11M8 1 11 4 8 7" fill="none" stroke="#16202a" stroke-width="1.2"/></svg></div>
  </div>
  <div class="dates">
    <div class="col" style="left:24px"><div class="lbl">Checkin Date:</div><div class="val">11th Nov 2017</div></div>
    <div class="div"></div>
    <div class="col" style="left:190px"><div class="lbl">Checkout Date:</div><div class="val">18th Nov 2017</div></div>
    <div class="btn">Check Rates &amp; Availability <svg width="14" height="8" viewBox="0 0 12 8"><path d="M0 4H11M8 1 11 4 8 7" fill="none" stroke="#fff" stroke-width="1.2"/></svg></div>
  </div>
</section>

<footer class="abs footer">
  <div class="foot-brand">Lumen.</div>
  <ul class="foot-contact">
    <li><svg width="13" height="10" viewBox="0 0 12 10"><rect x="0.6" y="0.6" width="10.8" height="8.8" fill="none" stroke="#b08d57" stroke-width="1.2"/><path d="M1 1.2 6 5.4 11 1.2" fill="none" stroke="#b08d57" stroke-width="1.2"/></svg>hello@lumenrooms.com</li>
    <li><svg width="12" height="12" viewBox="0 0 12 12"><path d="M2.5 1 4.6 1 5.4 3.6 4 4.6C4.8 6.3 5.7 7.2 7.4 8L8.4 6.6 11 7.4 11 9.5C11 10.4 10.3 11 9.5 11 5 11 1 7 1 2.5 1 1.7 1.6 1 2.5 1Z" fill="none" stroke="#b08d57" stroke-width="1.1"/></svg>+ 420 - 555 - 0182</li>
    <li><svg width="11" height="13" viewBox="0 0 10 13"><path d="M5 12C5 12 1 7.5 1 4.8A4 4 0 0 1 9 4.8C9 7.5 5 12 5 12Z" fill="none" stroke="#b08d57" stroke-width="1.2"/><circle cx="5" cy="4.8" r="1.4" fill="#b08d57"/></svg>Some address line goes here</li>
  </ul>
  <div class="foot-col" style="left:361px"><h4>Quick Links</h4><ul><li>How it works</li><li>Guarantee</li><li>Report Bug</li><li>Pricing</li></ul></div>
  <div class="foot-col" style="left:572px"><h4>About</h4><ul><li>About us</li><li>Team</li><li>Testimonials</li><li>Blogs</li></ul></div>
  <div class="foot-col" style="left:783px"><h4>Newsletter</h4><p>Subscribe to our email newsletter to get updates about offers &amp; discounts.</p></div>
  <div class="news">
    <div class="input"><svg width="12" height="9" viewBox="0 0 12 10"><rect x="0.6" y="0.6" width="10.8" height="8.8" fill="none" stroke="#b08d57" stroke-width="1.2"/><path d="M1 1.2 6 5.4 11 1.2" fill="none" stroke="#b08d57" stroke-width="1.2"/></svg>Enter email address</div>
    <div class="btn">Subscribe</div>
  </div>
</footer>
<div class="abs copyright">© 2017, All Rights Reserved.</div>

</body>
</html>
```